Brookvale Agribusiness Consulting needs a Website Design.

We need a website design for a new company based in UK. Brookvale offers agribusiness consulting and farm design services to farmers, smallholders and the wider agribusiness industry to assist clients in adopting more sustainable and regenerative production, processing and marketing practices.
Services are offered face-to-face and on a remote platform.
Services are offered in the UK and overseas.
We would like to see designs that reflect the natural environment, business and sustainability. Desired colours; green, blue, grey. The final design should communicate professionalism in the rural economy.
The design should be able to be customized by the client to make future changes and additions.
Target Market(s)
Farmers, smallholders, and the agricultural industry in UK and overseas.
Industry/Entity Type
Agribusiness
Number of Pages Required
4 page
Look and feel
Each slider illustrates characteristics of the customer's brand and the style your logo design should communicate.

```html
<!DOCTYPE html>
<html lang="en">
<head>
<meta charset="utf-8">
<title>Brookvale Agribusiness Consulting</title>
<link href="https://fonts.googleapis.com/css2?family=Open+Sans:wght@400;600;700;800&family=Lora:ital@1&display=swap" rel="stylesheet">
<style>
:root{
  --green:#7dc143;
  --teal:#1fa59a;
  --blue:#3d9fd9;
  --ink:#2b2b2b;
  --grey:#6f6f6f;
  --pale:#f0f0f0;
  --footer:#1f1f1f;
  --footer-deep:#121212;
  --footer-text:#a9a9a9;
}
*{box-sizing:border-box;margin:0;padding:0}
html,body{width:841px;height:1200px;overflow:hidden}
body{font-family:"Open Sans",Arial,sans-serif;background:#fff;color:var(--ink);position:relative}
.site-header{position:absolute;left:0;top:0;width:841px;height:84px;display:flex;align-items:center;padding:0 0 0 52px}
.brand{display:flex;align-items:center;gap:8px;font-weight:800;font-size:22px;color:var(--teal);letter-spacing:.5px;white-space:nowrap}
.brand-dot{width:22px;height:22px;border-radius:50%;background:var(--green)}
.main-nav{position:absolute;left:258px;top:0;display:flex;height:44px;white-space:nowrap}
.main-nav a{display:flex;align-items:center;padding:0 11px;font-size:10px;font-weight:700;color:var(--ink);text-decoration:none;letter-spacing:.3px}
.main-nav a.active{background:var(--teal);color:#fff;height:44px}
.phone-btn{position:absolute;left:642px;top:10px;height:26px;padding:0 14px;border-radius:13px;background:var(--green);color:#fff;font-size:12px;font-weight:600;display:flex;align-items:center;gap:6px;white-space:nowrap}
.hero{position:absolute;left:0;top:84px;width:841px;height:378px;background:linear-gradient(180deg,#8e9aa3 0%,#b9c2c7 45%,#c6ccc8 62%,#6f9a48 72%,#5e8a3a 100%)}
.hero-dots{position:absolute;right:34px;bottom:16px;display:flex;gap:5px}
.hero-dots span{width:8px;height:8px;border-radius:50%;background:#fff;opacity:.7}
.hero-dots span:first-child{opacity:1}
.section-title{position:absolute;left:0;top:488px;width:841px;text-align:center}
.section-title svg{display:block;margin:0 auto 2px}
.section-title h2{font-size:17px;font-weight:800;color:var(--ink);letter-spacing:.5px}
.section-title .underline{width:36px;height:3px;background:var(--green);margin:4px auto 0}
.service-card{position:absolute;top:552px;width:228px}
.service-photo{height:158px}
.service-label{height:34px;display:flex;align-items:center;justify-content:space-between;padding:0 10px 0 14px;color:#fff;font-size:13px;font-weight:600;letter-spacing:.3px}
.label-green{background:var(--green)}
.label-blue{background:var(--blue)}
.arrow-circle{width:20px;height:20px;border-radius:50%;background:#fff;display:flex;align-items:center;justify-content:center}
.welcome{position:absolute;left:0;top:772px;width:841px;height:194px;background:var(--pale)}
.welcome-heading{position:absolute;left:70px;top:30px;text-align:right;width:210px}
.welcome-heading .intro{font-family:"Lora",Georgia,serif;font-style:italic;font-size:18px;color:var(--grey)}
.welcome-heading .name{font-size:30px;font-weight:800;color:var(--ink);letter-spacing:.5px;margin-top:2px}
.welcome-text{position:absolute;left:340px;top:32px;width:450px;font-size:10px;line-height:1.65;color:var(--grey)}
.learn-btn{position:absolute;left:340px;top:150px;height:18px;padding:0 12px;background:var(--blue);color:#fff;font-size:8px;font-weight:700;border-radius:3px;display:flex;align-items:center}
.site-footer{position:absolute;left:0;top:974px;width:841px;height:226px;background:var(--footer);color:var(--footer-text);font-size:9px}
.footer-col{position:absolute;top:20px}
.footer-col h3{color:#fff;font-size:10px;font-weight:700;letter-spacing:.4px;margin-bottom:12px}
.news-item{margin-bottom:10px;line-height:1.5}
.news-item .date{color:var(--green)}
.quick-links li{list-style:none;line-height:1.9}
.contact-row{display:flex;gap:8px;align-items:flex-start;margin-bottom:10px;line-height:1.4}
.contact-icon{width:20px;height:20px;border-radius:50%;background:var(--green);flex:none;display:flex;align-items:center;justify-content:center}
.contact-phone{color:#fff;font-size:12px;font-weight:700}
.field{height:20px;background:#fff;border-radius:2px;color:#999;padding:0 6px;display:flex;align-items:center;margin-top:6px;font-size:8px}
.subscribe{height:20px;background:var(--teal);color:#fff;font-weight:700;font-size:9px;display:flex;align-items:center;justify-content:center;margin-top:6px;border-radius:2px}
.footer-bar{position:absolute;left:0;bottom:0;width:841px;height:30px;background:var(--footer-deep);display:flex;align-items:center;justify-content:space-between;padding:0 52px;font-size:8px}
.follow{display:flex;align-items:center;gap:6px}
.follow span.dot{width:14px;height:14px;border-radius:50%;background:var(--blue)}
</style>
</head>
<body>
<header class="site-header">
  <div class="brand"><span class="brand-dot"></span>BROOKVALE</div>
  <nav class="main-nav">
    <a class="active">HOME</a><a>ABOUT US</a><a>WHAT WE DO</a><a>SERVICES</a><a>CONTACT</a>
  </nav>
  <div class="phone-btn">
    <svg width="11" height="11" viewBox="0 0 24 24"><path fill="#fff" d="M6.6 10.8a15 15 0 0 0 6.6 6.6l2.2-2.2c.3-.3.7-.4 1-.2 1.1.4 2.3.6 3.6.6.6 0 1 .4 1 1V20c0 .6-.4 1-1 1A17 17 0 0 1 3 4c0-.6.4-1 1-1h3.5c.6 0 1 .4 1 1 0 1.2.2 2.4.6 3.6.1.3 0 .7-.2 1z"/></svg>
    (+44) 01632 960418
  </div>
</header>

<section class="hero" role="img" aria-label="Lone oak tree in a green field under a grey cloudy sky">
  <div class="hero-dots"><span></span><span></span><span></span></div>
</section>

<div class="section-title">
  <svg width="18" height="14" viewBox="0 0 18 14"><path d="M9 13C9 6 13 2 17 1c0 6-3 10-8 12z" fill="#7dc143"/><path d="M9 13C9 8 6 4 1 3c0 5 3 9 8 10z" fill="#1fa59a"/></svg>
  <h2>WHAT WE DO</h2>
  <div class="underline"></div>
</div>

<article class="service-card" style="left:50px">
  <div class="service-photo" role="img" aria-label="Cattle grazing in a green pasture" style="background:linear-gradient(180deg,#b7cfe0 0%,#6f8f4a 40%,#4d6e2e 100%)"></div>
  <div class="service-label label-green">CONSULTING<span class="arrow-circle"><svg width="8" height="8" viewBox="0 0 8 8"><path d="M2 1l3 3-3 3" stroke="#7dc143" stroke-width="1.6" fill="none"/></svg></span></div>
</article>
<article class="service-card" style="left:306px">
  <div class="service-photo" role="img" aria-label="Tray of fresh white eggs" style="background:radial-gradient(circle at 50% 50%,#f3eee6 0%,#ddd3c4 70%,#c7bba8 100%)"></div>
  <div class="service-label label-blue">PRODUCTION<span class="arrow-circle"><svg width="8" height="8" viewBox="0 0 8 8"><path d="M2 1l3 3-3 3" stroke="#3d9fd9" stroke-width="1.6" fill="none"/></svg></span></div>
</article>
<article class="service-card" style="left:562px">
  <div class="service-photo" role="img" aria-label="Fresh vegetables displayed at a market stall" style="background:linear-gradient(135deg,#6f9a3e 0%,#c24a2e 45%,#d9a23a 70%,#7a5a3a 100%)"></div>
  <div class="service-label label-green">MARKETING<span class="arrow-circle"><svg width="8" height="8" viewBox="0 0 8 8"><path d="M2 1l3 3-3 3" stroke="#7dc143" stroke-width="1.6" fill="none"/></svg></span></div>
</article>

<section class="welcome">
  <div class="welcome-heading">
    <div class="intro">Welcome to</div>
    <div class="name">BROOKVALE</div>
  </div>
  <p class="welcome-text">Brookvale works alongside farmers, smallholders and agribusinesses to build sustainable and regenerative systems that protect soil, water and margins. From whole-farm design to processing and marketing plans, our consultants bring practical field experience and clear advice. We support clients face-to-face across the UK and remotely overseas, helping each enterprise grow healthier land, stronger supply chains and a more profitable rural economy for the next generation of growers and the communities around them.</p>
  <div class="learn-btn">LEARN MORE</div>
</section>

<footer class="site-footer">
  <div class="footer-col" style="left:52px;width:170px">
    <h3>RECENT NEWS</h3>
    <div class="news-item"><div class="date">14 March 2014</div>Soil health field day announced for spring growers.</div>
    <div class="news-item"><div class="date">02 March 2014</div>New guide to regenerative grazing now available.</div>
  </div>
  <div class="footer-col" style="left:242px;width:120px">
    <h3>QUICK LINKS</h3>
    <ul class="quick-links"><li>Home</li><li>About us</li><li>What we do</li><li>Services</li><li>Contact</li></ul>
  </div>
  <div class="footer-col" style="left:412px;width:170px">
    <h3>GET IN TOUCH</h3>
    <div class="contact-row"><span class="contact-icon"><svg width="9" height="11" viewBox="0 0 10 12"><path d="M5 0a4 4 0 0 0-4 4c0 3 4 8 4 8s4-5 4-8a4 4 0 0 0-4-4zm0 5.5A1.5 1.5 0 1 1 5 2.5a1.5 1.5 0 0 1 0 3z" fill="#fff"/></svg></span><span>12 Mill Lane,<br>Exeter EX1 4QT</span></div>
    <div class="contact-row"><span class="contact-icon"><svg width="10" height="10" viewBox="0 0 24 24"><path fill="#fff" d="M6.6 10.8a15 15 0 0 0 6.6 6.6l2.2-2.2c.3-.3.7-.4 1-.2 1.1.4 2.3.6 3.6.6.6 0 1 .4 1 1V20c0 .6-.4 1-1 1A17 17 0 0 1 3 4c0-.6.4-1 1-1h3.5c.6 0 1 .4 1 1 0 1.2.2 2.4.6 3.6.1.3 0 .7-.2 1z"/></svg></span><span>Phone:<br><span class="contact-phone">(+44) 01632 960418</span></span></div>
    <div class="contact-row"><span class="contact-icon"><svg width="10" height="8" viewBox="0 0 12 9"><rect x=".5" y=".5" width="11" height="8" fill="none" stroke="#fff"/><path d="M.5.5 6 5l5.5-4.5" fill="none" stroke="#fff"/></svg></span><span>Email:<br>info@brookvale.co.uk</span></div>
  </div>
  <div class="footer-col" style="left:618px;width:170px">
    <h3>NEWSLETTER SIGNUP</h3>
    <p style="line-height:1.5">Sign up to receive our monthly updates on regenerative farming news and events.</p>
    <div class="field">Enter Your Name</div>
    <div class="field">Enter Your Email</div>
    <div class="subscribe">SUBSCRIBE</div>
  </div>
  <div class="footer-bar">
    <span>© 2013 Brookvale. All Rights Reserved &nbsp;|&nbsp; Terms and Conditions &nbsp;|&nbsp; Privacy Policy &nbsp;|&nbsp; Terms of Use</span>
    <span class="follow">Follow us on <span class="dot"></span></span>
  </div>
</footer>
</body>
</html>
```